I need a logo design and a business card design for a new strategy consultancy that I set up called Corvanel LLC. We help clients make strategically important decisions, cutting through the cloud of noise. The design should imply clarity, simplicity and wisdom.

```html
<!DOCTYPE html>
<html lang="en">
<head>
<meta charset="utf-8">
<title>Corvanel LLC – Business Cards</title>
<link href="https://fonts.googleapis.com/css2?family=Lato:wght@400;700&display=swap" rel="stylesheet">
<style>
  :root {
    --backdrop: #2a2a2c;
    --teal: #22b4ca;
    --teal-light: #2fc3d6;
    --teal-deep: #1a9fb3;
    --paper: #f7f7f7;
    --paper-edge: #e6e6e6;
    --ink-grey: #6b6b6b;
    --ink-dark: #444;
    --white: #ffffff;
  }
  * { margin: 0; padding: 0; box-sizing: border-box; }
  html, body {
    width: 1200px; height: 900px; overflow: hidden;
    background: var(--backdrop);
    font-family: "Lato", Arial, sans-serif;
  }
  .canvas { position: relative; width: 1200px; height: 900px; }
  .card {
    position: absolute;
    width: 600px; height: 343px;
    border-radius: 26px;
    box-shadow: 0 14px 30px rgba(0,0,0,0.45);
    overflow: hidden;
  }
  .card--front {
    left: 110px; top: 110px;
    background: radial-gradient(ellipse at 55% 45%, var(--teal-light) 0%, var(--teal) 55%, var(--teal-deep) 100%);
    display: flex; align-items: center; justify-content: center;
  }
  .card--back {
    left: 490px; top: 450px;
    background: radial-gradient(ellipse at 50% 40%, var(--white) 0%, var(--paper) 60%, var(--paper-edge) 100%);
  }
  .wordmark {
    font-weight: 700;
    letter-spacing: 0.08em;
    text-transform: uppercase;
    white-space: nowrap;
  }
  .card--front .wordmark { color: var(--white); font-size: 44px; }
  .card--back .wordmark {
    position: absolute; left: 60px; top: 148px;
    color: var(--teal); font-size: 32px;
  }
  .identity {
    position: absolute; left: 345px; top: 104px;
  }
  .identity__name {
    font-size: 22px; font-weight: 400; color: var(--ink-grey);
    letter-spacing: 0.02em; text-transform: uppercase;
  }
  .identity__title {
    font-size: 14px; font-weight: 400; color: var(--teal);
    text-transform: uppercase; margin-top: 2px;
  }
  .contact { list-style: none; margin-top: 18px; }
  .contact__item {
    display: flex; align-items: center; gap: 8px;
    font-size: 13px; color: var(--ink-dark); line-height: 20px;
  }
  .contact__icon { width: 12px; height: 12px; flex: none; }
</style>
</head>
<body>
<main class="canvas">
  <section class="card card--front" aria-label="Card front">
    <span class="wordmark">Corvanel LLC</span>
  </section>

  <section class="card card--back" aria-label="Card back">
    <span class="wordmark">Corvanel LLC</span>
    <div class="identity">
      <p class="identity__name">Your Name</p>
      <p class="identity__title">Job Title</p>
      <ul class="contact">
        <li class="contact__item">
          <svg class="contact__icon" viewBox="0 0 12 12" aria-hidden="true">
            <path d="M1 4 Q6 0 11 4 L9.5 5.5 L8 4.5 L8 3.5 Q6 3 4 3.5 L4 4.5 L2.5 5.5 Z" fill="#22b4ca"/>
            <rect x="2.5" y="6" width="7" height="5" rx="1" fill="#22b4ca"/>
          </svg>
          000 000 0000
        </li>
        <li class="contact__item">
          <svg class="contact__icon" viewBox="0 0 12 12" aria-hidden="true">
            <rect x="0.5" y="2.5" width="11" height="7.5" fill="#22b4ca"/>
            <path d="M0.5 2.5 L6 7 L11.5 2.5" fill="none" stroke="#fff" stroke-width="1"/>
          </svg>
          youremail@xyz.com
        </li>
        <li class="contact__item">
          <svg class="contact__icon" viewBox="0 0 12 12" aria-hidden="true">
            <circle cx="6" cy="6" r="5" fill="none" stroke="#22b4ca" stroke-width="1"/>
            <ellipse cx="6" cy="6" rx="2.2" ry="5" fill="none" stroke="#22b4ca" stroke-width="0.8"/>
            <line x1="1" y1="6" x2="11" y2="6" stroke="#22b4ca" stroke-width="0.8"/>
          </svg>
          www.yourwebsite.com
        </li>
      </ul>
    </div>
  </section>
</main>
</body>
</html>
```